Velmora Company needs a Business Card Design

We just opened our business recently and we need a business card design. Our basic product are clothes and accessories. We would like to see designs that use bright colors like pink, light blue and purple. In addition to that kindly include also our address in the business card which our main office is located in Los Angeles, California.
The final design should communicate that we have affordable price yet high quality brand.

Target Market(s)

young and middle age women

Industry/Entity Type

Business

Contact Information for Business Card

Velmora Apparel and Accessories 3847 North Hollis St. Los Angeles California
Tel: 424-583-6094

Logo Text

Velmora's Apparel and Accessories

Font styles to use
Serif

Requirements
Must have
• there should be a graphic of a sexy lady wearing an elegant dress at the upper left corner of the business card.

```html
<!DOCTYPE html>
<html lang="en">
<head>
<meta charset="utf-8">
<title>Velmora Apparel and Accessories – Business Card</title>
<link rel="stylesheet" href="https://fonts.googleapis.com/css2?family=Comfortaa:wght@600&family=Italianno&family=Tinos&display=swap">
<style>
  :root {
    --page-bg: #e9e7e4;
    --card-bg: #ffffff;
    --card-edge: #f1f1f1;
    --brand-pink: #e8339f;
    --ink: #1c1c1c;
    --sketch-tone: #eceef0;
    --figure-hair: #8a4a32;
    --figure-shirt: #f4f2f2;
    --figure-denim: #9ccbe3;
    --figure-skin: #f1d5bd;
  }
  * { box-sizing: border-box; margin: 0; padding: 0; }
  html, body {
    width: 1200px;
    height: 1023px;
    overflow: hidden;
  }
  body {
    background: var(--page-bg);
    display: flex;
    align-items: center;
    justify-content: center;
  }
  .business-card {
    position: relative;
    width: 910px;
    height: 520px;
    background: var(--card-bg);
    border: 1px solid var(--card-edge);
    box-shadow: 0 10px 30px rgba(0,0,0,0.12);
    overflow: hidden;
  }
  .city-sketch-backdrop {
    position: absolute;
    inset: 0;
    background: linear-gradient(160deg, #ffffff 0%, var(--sketch-tone) 55%, #ffffff 100%);
    opacity: 0.8;
  }
  .fashion-figure {
    position: absolute;
    left: 40px;
    top: 28px;
    width: 230px;
    height: 464px;
    border-radius: 110px 110px 24px 24px;
    background: linear-gradient(180deg,
      var(--figure-hair) 0%,
      var(--figure-skin) 18%,
      var(--figure-shirt) 30%,
      var(--figure-shirt) 55%,
      var(--figure-denim) 68%,
      var(--figure-skin) 80%,
      var(--figure-hair) 100%);
    opacity: 0.85;
  }
  .card-copy {
    position: absolute;
    left: 330px;
    top: 70px;
    right: 40px;
  }
  .brand-name {
    font-family: "Comfortaa", sans-serif;
    font-weight: 600;
    font-size: 124px;
    line-height: 1;
    color: var(--brand-pink);
    letter-spacing: 2px;
  }
  .brand-tagline {
    margin-top: 14px;
    font-family: "Italianno", cursive;
    font-size: 56px;
    line-height: 1;
    color: var(--ink);
    letter-spacing: 3px;
  }
  .contact-phone,
  .contact-address {
    font-family: "Tinos", serif;
    font-size: 26px;
    color: var(--ink);
  }
  .contact-phone { margin-top: 34px; padding-left: 120px; }
  .contact-address { margin-top: 14px; }
</style>
</head>
<body>
  <article class="business-card">
    <div class="city-sketch-backdrop" role="img" aria-label="Faint line sketch of a city street scene"></div>
    <div class="fashion-figure" role="img" aria-label="Illustration of a stylish young woman in a cap, sunglasses, slogan tee and denim shorts carrying a bag"></div>
    <div class="card-copy">
      <h1 class="brand-name">Velmora</h1>
      <p class="brand-tagline">Apparel &amp; Accessories</p>
      <p class="contact-phone">424-583-6094</p>
      <p class="contact-address">3847 North Hollis St. Los Angeles California</p>
    </div>
  </article>
</body>
</html>
```